Design New Business Card, Envelope and Letter Head !

We need a stationery design for our newly developed logo! We need professional classic look.

Front of the Card:
Logo on the left hand side

Personal Detail in the right hand side
i.e. Name,
Title
Office:
Cell:
Fax:
email:

www.torvanlending.example

Color Scheme should match our logo.

Back Side of the Card:

Logo again with Green back ground or off gray back ground ( Note: Color has to be from logo)

and below message. Again, font size and color should come from logo.

" Manifest your trust in us through the gift of your referrals. We won't let you down."
Updates

Dear Designers;

We have updates few info which we missed earlier. Please include those words in the logo and resubmit your designs for consideration.  We are looking for very professional and classic look. Thanks for your great creation. I have changed the payment options. Please have a look and best of luck.

Ned

Dear All Designers:

For address; please use following address:

" 4172 Willow Crest Ln, San Ramon, CA 94583 " 
Please do not use the address in the website. We would like to give business card with option of calling us is the top priority then email then qLine. Please make sure Put " qLine" in the business card. 

Reason: Since I have updated some information per requirements, I would like to give enough time for the great design work.

Just a note to all designers:

"Equal Opportunity Lender" Sign has to be in back  of the card  in a small image. I would say it has to be "inconspicuous". Let's put the HRQA # and StaPLO # in front side. Let's organise the information follow very elegant and professional.

Requirements
Must have
• We must need following Words in the business card

StaPLO License #

HRQA #

And the logo of " Equal Housing Lender ". Please see the logo attached.

Please put these words or logo represents above at the right location of the card.

```html
<!DOCTYPE html>
<html lang="en">
<head>
<meta charset="utf-8">
<title>Torvan Lending Business Card</title>
<link href="https://fonts.googleapis.com/css2?family=Tinos:wght@400&display=swap" rel="stylesheet">
<style>
  :root {
    --green: #5a9e2c;
    --ink: #4a4a4a;
    --card-light: #eeeeee;
    --band-gray: #555555;
    --white: #ffffff;
    --backdrop: #e4e2de;
  }
  * { margin: 0; padding: 0; box-sizing: border-box; }
  html, body { width: 1200px; height: 900px; overflow: hidden; }
  body {
    background: var(--backdrop);
    font-family: "Tinos", "Times New Roman", serif;
    position: relative;
  }
  .card {
    position: absolute;
    left: 300px;
    width: 600px;
    height: 336px;
    overflow: hidden;
    box-shadow: 0 3px 8px rgba(0,0,0,0.25);
  }
  .card-front { top: 96px; background: var(--card-light); color: var(--ink); }
  .card-back { top: 468px; background: var(--green); color: var(--white); }

  .brand { position: absolute; display: flex; align-items: center; }
  .brand-mark { width: 18px; height: 18px; margin-right: 16px; }
  .brand-name { font-size: 46px; line-height: 1; white-space: nowrap; }
  .brand-tagline {
    position: absolute; font-size: 11px; letter-spacing: 3.6px; white-space: nowrap;
  }
  .card-front .brand { left: 130px; top: 28px; }
  .card-front .brand-mark { background: var(--green); }
  .card-front .brand-name { color: var(--ink); border-bottom: 1px solid var(--ink); padding-bottom: 4px; }
  .card-front .brand-tagline { left: 172px; top: 80px; color: var(--ink); }

  .person { position: absolute; left: 62px; top: 128px; }
  .person-name { font-size: 27px; line-height: 1.1; }
  .person-title { font-size: 15px; margin-top: 6px; }

  .contact { position: absolute; left: 327px; top: 138px; font-size: 15px; line-height: 19px; }
  .contact-row { display: flex; }
  .contact-label { color: var(--green); width: 55px; }
  .address { margin-top: 13px; }
  .website { margin-top: 13px; }

  .front-band { position: absolute; left: 0; bottom: 0; width: 600px; height: 22px; }

  .card-back .brand { left: 40px; top: 102px; }
  .card-back .brand-mark { background: var(--white); margin-right: 100px; }
  .card-back .brand-name { color: var(--white); border-bottom: 1px solid var(--white); padding-bottom: 4px; }
  .card-back .brand-tagline { left: 160px; top: 158px; color: var(--white); }

  .referral {
    position: absolute; left: 0; width: 600px; top: 196px;
    text-align: center; font-size: 18px; line-height: 23px;
  }
  .licenses {
    position: absolute; left: 0; width: 600px; top: 278px;
    display: flex; justify-content: center; align-items: center; gap: 16px;
    font-size: 13px;
  }
  .lender-badge { width: 30px; height: 30px; border: 2px solid var(--white); border-radius: 3px; }
</style>
</head>
<body>
  <section class="card card-front">
    <div class="brand">
      <span class="brand-mark"></span>
      <span class="brand-name">Torvan Lending</span>
    </div>
    <div class="brand-tagline">YOUR TRUSTED MORTGAGE ADVISORS</div>

    <div class="person">
      <div class="person-name">Dev Marwah</div>
      <div class="person-title">Real Estate Entrepreneur</div>
    </div>

    <div class="contact">
      <div class="contact-row"><span class="contact-label">Office</span><span>925-555-0147</span></div>
      <div class="contact-row"><span class="contact-label">Cell</span><span>510-555-0183</span></div>
      <div class="contact-row"><span class="contact-label">Fax</span><span>925-555-0162</span></div>
      <div class="contact-row"><span class="contact-label">Email</span><span>dev@torvanlending.example</span></div>
      <div class="address">4172 Willow Crest Ln.<br>San Ramon, CA 94583</div>
      <div class="website">www.torvanlending.example</div>
    </div>

    <svg class="front-band" viewBox="0 0 600 22" aria-hidden="true">
      <polygon points="0,0 312,0 295,22 0,22" fill="var(--band-gray)"/>
      <polygon points="326,0 600,0 600,22 309,22" fill="var(--green)"/>
    </svg>
  </section>

  <section class="card card-back">
    <div class="brand">
      <span class="brand-mark"></span>
      <span class="brand-name">Torvan Lending</span>
    </div>
    <div class="brand-tagline">YOUR TRUSTED MORTGAGE ADVISORS</div>

    <p class="referral">Manifest your trust in us through the gift of your referrals.<br>WE WON'T LET YOU DOWN.</p>

    <div class="licenses">
      <span>StaPLO # 02471583</span>
      <span class="lender-badge" role="img" aria-label="Equal housing lender badge"></span>
      <span>HRQA # 418266</span>
    </div>
  </section>
</body>
</html>
```